Website Re-Design

We would like to explore the possibility of a re-design of our website. We want all the content that it currently has to remain on the pages, and we don't want our logo/corporate identity or colours changed, so it is literally just a website re-design.

Our website is www.drelvix.co.uk

Websites that we like are

http://www.tarnwillow.co.uk/
http://quomplet.com/

```html
<!DOCTYPE html>
<html lang="en">
<head>
<meta charset="utf-8">
<title>Drelvix – Inbound Marketing &amp; SEO Performance Agency</title>
<link href="https://fonts.googleapis.com/css2?family=Montserrat:wght@400;600;700;800&family=Open+Sans:wght@400;600&display=swap" rel="stylesheet">
<style>
:root{
  --pink:#e6007e;
  --green:#8cc63f;
  --teal:#16a99c;
  --dark:#2a2a2a;
  --darker:#1f1f1f;
  --grey:#dcdcdc;
  --light:#f1f1f1;
  --text:#bdbdbd;
  --white:#ffffff;
}
*{box-sizing:border-box;margin:0;padding:0}
html,body{width:720px;height:1200px;overflow:hidden;background:var(--white)}
body{font-family:"Open Sans",Arial,sans-serif;color:#555;position:relative}
.page{position:absolute;inset:0;width:720px;height:1200px}

/* header */
.site-header{height:75px;display:flex;align-items:center;justify-content:space-between;padding:0 40px;border-top:4px solid var(--pink)}
.brand{display:flex;flex-direction:column;line-height:1}
.brand-name{font-family:"Montserrat",sans-serif;font-weight:800;font-size:26px;color:var(--green);letter-spacing:1px}
.brand-sub{font-size:6px;color:var(--pink);margin-top:3px;letter-spacing:.5px}
.main-nav{display:flex;gap:16px}
.nav-item{display:flex;flex-direction:column;align-items:center;font-size:8px;color:#666;gap:4px}
.nav-icon{width:28px;height:28px;border-radius:50%;background:var(--green);display:flex;align-items:center;justify-content:center}

/* hero */
.hero{position:relative;height:225px;background:linear-gradient(135deg,#c9ccd0,#9ea3a8 55%,#7d8388)}
.hero-photo{position:absolute;inset:0}
.hero-copy{position:absolute;left:110px;top:40px;width:330px}
.hero-title{font-family:"Montserrat",sans-serif;font-weight:700;font-size:17px;line-height:1.2;color:var(--white);text-transform:uppercase;letter-spacing:.5px}
.hero-title span{color:var(--pink)}
.cta{display:inline-block;margin-top:14px;background:var(--pink);color:var(--white);font-family:"Montserrat",sans-serif;font-weight:800;font-size:20px;padding:7px 16px;text-transform:uppercase}
.hero-arrow{position:absolute;top:80px;color:var(--white);font-size:30px;font-family:"Montserrat",sans-serif}
.hero-arrow.prev{left:14px}.hero-arrow.next{right:14px}
.service-bar{position:absolute;left:0;right:0;bottom:0;height:38px;background:var(--green);color:var(--white);font-family:"Montserrat",sans-serif;font-weight:600;font-size:15px;display:flex;align-items:center;padding-left:40px;letter-spacing:.3px}

/* dark area */
.dark-area{background:var(--dark);height:440px;position:relative}
.tagline{height:44px;border-bottom:1px solid #3a3a3a;display:flex;flex-direction:column;justify-content:center;padding-left:40px}
.tagline h1{font-family:"Montserrat",sans-serif;font-weight:600;font-size:15px;color:var(--green)}
.tagline p{font-size:7px;color:var(--text);margin-top:3px}
.features{display:flex;justify-content:space-around;padding:18px 40px 0}
.feature{width:170px;text-align:center}
.feature h2{font-family:"Montserrat",sans-serif;font-size:12px;color:var(--white);font-weight:600}
.feature-icon{width:52px;height:52px;border-radius:50%;margin:12px auto;display:flex;align-items:center;justify-content:center;border:3px solid var(--white)}
.feature-icon.pink{background:var(--pink)}.feature-icon.green{background:var(--green)}.feature-icon.teal{background:var(--teal)}
.feature p{font-size:7px;color:var(--text);line-height:1.4}
.more{display:inline-block;margin-top:8px;background:#555;color:#ddd;font-size:7px;padding:2px 10px;border-radius:2px}
.clients{text-align:center;margin-top:34px}
.clients h2{font-family:"Montserrat",sans-serif;font-size:20px;color:var(--green);font-weight:700}
.clients p{font-size:7px;color:var(--text);margin-top:4px}
.client-row{display:flex;justify-content:center;gap:12px;margin-top:16px;align-items:center}
.client{width:62px;height:56px;background:var(--white);display:flex;align-items:center;justify-content:center;font-family:"Open Sans",sans-serif;font-weight:600;font-size:9px;color:#444}
.client.plus{font-size:18px;color:#999}
.row-arrow{color:#777;font-size:22px;font-family:"Montserrat",sans-serif}
.side-dot{position:absolute;right:4px;width:14px;height:14px;border-radius:50%;background:#eee;border:2px solid #555}

/* contact */
.contact{background:var(--light);height:270px;position:relative}
.phone-art{position:absolute;left:140px;top:24px;width:70px;height:78px;background:linear-gradient(160deg,#2d3a6b,#16a99c);border-radius:8px}
.contact-head{position:absolute;left:230px;top:40px;text-align:center;width:280px}
.contact-head h2{font-family:"Montserrat",sans-serif;font-size:17px;color:#444;font-weight:700}
.contact-head p{font-size:7px;color:#888;letter-spacing:1px;margin-top:2px}
.contact-lines{position:absolute;top:110px;left:150px;right:120px;display:flex;justify-content:space-between;font-family:"Montserrat",sans-serif;font-size:17px;color:var(--green)}
.contact-lines span{display:flex;align-items:center;gap:8px}
.testimonial{position:absolute;left:170px;top:150px;width:380px;height:62px;background:var(--white);border:1px solid #ddd;padding:8px 12px;font-size:7px;color:#888;line-height:1.4;text-align:center}
.testimonial cite{display:block;text-align:right;font-size:6px;margin-top:4px;font-style:normal}
.social{position:absolute;top:226px;left:0;right:0;display:flex;justify-content:center;gap:8px}
.social span{width:22px;height:22px;border-radius:50%;background:#888}

/* footer */
.site-footer{background:var(--darker);height:185px;color:#aaa;font-size:7px;position:relative;padding:14px 40px 0;display:flex;gap:26px}
.site-footer h3{font-family:"Montserrat",sans-serif;font-size:9px;color:var(--white);margin-bottom:8px;font-weight:600}
.footer-col ul{list-style:none;line-height:1.9}
.col-links{width:70px}.col-contact{width:150px;line-height:1.9}.col-about{width:150px;line-height:1.5}
.col-work{width:170px}
.work-art{height:90px;background:linear-gradient(135deg,#e6007e,#5a2a7a 60%,#2a2a2a)}
.work-caption{margin-top:4px}
.copyright{position:absolute;bottom:8px;left:0;right:0;text-align:center;font-size:6px;color:#777}
</style>
</head>
<body>
<div class="page">
  <header class="site-header">
    <div class="brand">
      <span class="brand-name">DRELVIX</span>
      <span class="brand-sub">INBOUND MARKETING &amp; SEO PERFORMANCE AGENCY</span>
    </div>
    <nav class="main-nav">
      <div class="nav-item"><span class="nav-icon"><svg width="14" height="14" viewBox="0 0 14 14"><path d="M2 7 7 2l5 5v5H9V9H5v3H2z" fill="#fff"/></svg></span>Home</div>
      <div class="nav-item"><span class="nav-icon"><svg width="14" height="14" viewBox="0 0 14 14"><rect x="3" y="2" width="8" height="10" fill="#fff"/></svg></span>Blog</div>
      <div class="nav-item"><span class="nav-icon"><svg width="14" height="14" viewBox="0 0 14 14"><circle cx="7" cy="5" r="2.5" fill="#fff"/><path d="M2 13c0-3 2.5-4.5 5-4.5s5 1.5 5 4.5z" fill="#fff"/></svg></span>About</div>
      <div class="nav-item"><span class="nav-icon"><svg width="14" height="14" viewBox="0 0 14 14"><rect x="2" y="4" width="10" height="8" fill="#fff"/><rect x="5" y="2" width="4" height="2" fill="#fff"/></svg></span>Portfolio</div>
      <div class="nav-item"><span class="nav-icon"><svg width="14" height="14" viewBox="0 0 14 14"><circle cx="7" cy="7" r="4" fill="none" stroke="#fff" stroke-width="2"/></svg></span>What we do</div>
      <div class="nav-item"><span class="nav-icon"><svg width="14" height="14" viewBox="0 0 14 14"><rect x="2" y="3" width="10" height="8" fill="#fff"/><path d="M2 3l5 4 5-4" stroke="#8cc63f" fill="none"/></svg></span>Contact us</div>
    </nav>
  </header>

  <section class="hero">
    <div class="hero-photo" role="img" aria-label="Photo of a bright city street with office buildings"></div>
    <span class="hero-arrow prev">‹</span>
    <div class="hero-copy">
      <p class="hero-title">Drelvix take a holistic view <span>of earning your customers attention</span></p>
      <span class="cta">Get started now!</span>
    </div>
    <span class="hero-arrow next">›</span>
    <div class="service-bar">SEO / CONSULTANSY / CRO / SOCIAL CAMPAIGN / CREATIVES</div>
  </section>

  <section class="dark-area">
    <div class="tagline">
      <h1>Drelvix - your inbound marketing &amp; SEO performance agency</h1>
      <p>Drelvix is an inbound marketing agency focused on search, content and conversion for growing brands.</p>
    </div>
    <div class="features">
      <div class="feature">
        <h2>WHAT WE DO</h2>
        <div class="feature-icon pink"><svg width="22" height="22" viewBox="0 0 22 22"><circle cx="11" cy="11" r="7" fill="none" stroke="#fff" stroke-width="3"/><circle cx="11" cy="11" r="2" fill="#fff"/></svg></div>
        <p>We offer a bespoke service and will customise to your needs.</p>
        <span class="more">more</span>
      </div>
      <div class="feature">
        <h2>OUR WORK</h2>
        <div class="feature-icon green"><svg width="24" height="20" viewBox="0 0 24 20"><rect x="2" y="2" width="20" height="13" fill="none" stroke="#fff" stroke-width="2"/><rect x="8" y="16" width="8" height="2" fill="#fff"/></svg></div>
        <p>Take a look at our recent work and see the results we deliver.</p>
        <span class="more">more</span>
      </div>
      <div class="feature">
        <h2>LET'S TALK</h2>
        <div class="feature-icon teal"><svg width="22" height="20" viewBox="0 0 22 20"><path d="M2 2h18v11H9l-5 4v-4H2z" fill="#fff"/></svg></div>
        <p>Get in touch and we will arrange a call to discuss your goals.</p>
        <span class="more">more</span>
      </div>
    </div>
    <div class="clients">
      <h2>OUR CLIENTS</h2>
      <p>We work with brands of every size across retail, travel and finance.</p>
      <div class="client-row">
        <span class="row-arrow">‹</span>
        <span class="client">Stayvora</span>
        <span class="client">Brookfen</span>
        <span class="client">Calderon</span>
        <span class="client">Pexmoor</span>
        <span class="client plus">+</span>
        <span class="row-arrow">›</span>
      </div>
    </div>
    <span class="side-dot" style="top:190px"></span>
  </section>

  <section class="contact">
    <div class="phone-art" role="img" aria-label="Illustration of a hand holding a smartphone"></div>
    <div class="contact-head">
      <h2>SOUNDS INTERESTING!</h2>
      <p>WE WOULD LOVE TO HEAR FROM YOU</p>
    </div>
    <div class="contact-lines">
      <span><svg width="14" height="14" viewBox="0 0 14 14"><path d="M3 1l3 3-2 2c1 2 2 3 4 4l2-2 3 3-2 2C6 13 1 8 1 3z" fill="#8cc63f"/></svg>+44 101 207 481 3370</span>
      <span><svg width="16" height="12" viewBox="0 0 16 12"><rect x="1" y="1" width="14" height="10" fill="none" stroke="#8cc63f" stroke-width="1.5"/><path d="M1 1l7 5 7-5" fill="none" stroke="#8cc63f" stroke-width="1.5"/></svg>hello@drelvix.co.uk</span>
    </div>
    <blockquote class="testimonial">
      Drelvix helped us grow organic traffic quickly and the team were a pleasure to work with from start to finish.
      <cite>Client name, Marketing Lead</cite>
    </blockquote>
    <div class="social"><span></span><span></span><span></span><span></span><span></span><span></span></div>
  </section>

  <footer class="site-footer">
    <div class="footer-col col-links">
      <h3>DRELVIX</h3>
      <ul><li>Home</li><li>About</li><li>Blog</li><li>Portfolio</li><li>Services</li><li>Contact Us</li></ul>
    </div>
    <div class="footer-col col-contact">
      <h3>CONTACT US</h3>
      The Larkmoor Mews, Quill Street, London, EC1 4RT<br>
      www.drelvix.co.uk<br>
      hello@drelvix.co.uk<br>
      +44 101 207 481 3370
    </div>
    <div class="footer-col col-about">
      <h3>ABOUT</h3>
      Drelvix is an inbound marketing agency offering SEO, CRO, social media and creative services to ambitious brands.
    </div>
    <div class="footer-col col-work">
      <h3>RECENT WORK</h3>
      <div class="work-art" role="img" aria-label="Infographic artwork from a recent project"></div>
      <p class="work-caption">Infographic design for a travel client</p>
    </div>
    <p class="copyright">Copyright © 2024 Drelvix. All rights reserved.</p>
  </footer>
</div>
</body>
</html>
```